Demolition Company Billboard Design 13 feet wide 15 feet high

This is my first billboard on a busy road. I want it to be professional but with some eye catching flair that matches by business which is a demoltion business and also list my services. My company slogan is also

"call quill to clear the hill"

Target Market(s)

Home Ownerd and General Construction Companies

Industry/Entity Type

construction

Colors
0054AA
0677BA
7BADD7
CADEEF
E8F1F8

Requirements
Must have
• My services listed in the pictures my website and my phone number

```html
<!DOCTYPE html>
<html lang="en">
<head>
<meta charset="utf-8">
<title>Quill Clearing Billboard</title>
<link rel="stylesheet" href="https://fonts.googleapis.com/css2?family=Anton&family=Oswald:wght@400;500;700&display=swap">
<style>
  :root {
    --page: #f8f8f8;
    --photo-top: #2f649c;
    --photo-mid: #24486f;
    --photo-low: #172c45;
    --ink: #ffffff;
    --accent: #ffcc00;
    --base: #000000;
  }
  html, body {
    margin: 0;
    padding: 0;
    width: 1200px;
    height: 1200px;
    overflow: hidden;
    background: var(--page);
  }
  .billboard {
    position: absolute;
    left: 185px;
    top: 121px;
    width: 837.5px;
    height: 966px;
    overflow: hidden;
  }
  .site-photo {
    position: absolute;
    inset: 0;
    background: linear-gradient(180deg, var(--photo-top) 0%, var(--photo-mid) 45%, var(--photo-low) 100%);
  }
  .artwork {
    position: absolute;
    inset: 0;
    width: 100%;
    height: 100%;
  }
  .brand-name {
    font-family: "Oswald", sans-serif;
    font-weight: 500;
    font-size: 46px;
    letter-spacing: 3px;
    fill: var(--ink);
  }
  .slogan {
    font-family: "Anton", sans-serif;
    fill: var(--ink);
  }
  .services {
    font-family: "Oswald", sans-serif;
    font-weight: 400;
    font-size: 54px;
    fill: var(--ink);
  }
  .web {
    font-family: "Oswald", sans-serif;
    font-weight: 500;
    font-size: 40px;
    fill: var(--ink);
  }
  .phone {
    font-family: "Oswald", sans-serif;
    font-weight: 700;
    font-size: 62px;
    fill: var(--ink);
  }
  .icon {
    fill: none;
    stroke: var(--ink);
    stroke-width: 3;
    stroke-linecap: round;
    stroke-linejoin: round;
  }
</style>
</head>
<body>
  <main class="billboard">
    <div class="site-photo" role="img" aria-label="Photo of an excavator demolishing the steel frame of a large industrial building, tinted blue"></div>

    <svg class="artwork" viewBox="0 0 837.5 966" xmlns="http://www.w3.org/2000/svg">
      <text class="brand-name" x="418.75" y="152" text-anchor="middle">QUILL CLEARING</text>

      <text class="slogan" x="48" y="330" font-size="118" textLength="700" lengthAdjust="spacingAndGlyphs">"CALL QUILL TO</text>
      <text class="slogan" x="118" y="463" font-size="118" textLength="670" lengthAdjust="spacingAndGlyphs">CLEAR THE HILL”</text>

      <g class="service-list">
        <circle cx="61" cy="636" r="9" fill="#ffffff"/>
        <text class="services" x="82" y="657" textLength="172" lengthAdjust="spacingAndGlyphs">INTERIOR</text>
        <circle cx="286" cy="636" r="9" fill="#ffffff"/>
        <text class="services" x="307" y="657" textLength="178" lengthAdjust="spacingAndGlyphs">EXTERIOR</text>
        <circle cx="509" cy="636" r="9" fill="#ffffff"/>
        <text class="services" x="532" y="657" textLength="253" lengthAdjust="spacingAndGlyphs">COMMERCIAL</text>
      </g>

      <polygon class="accent-band" points="0,818 159,697 837.5,830 837.5,966 0,966" fill="var(--accent)"/>
      <polygon class="contact-band" points="0,837 157.5,729 837.5,847 837.5,966 0,966" fill="var(--base)"/>

      <g class="icon globe" transform="translate(78 889)">
        <circle r="24"/>
        <ellipse rx="11" ry="24"/>
        <line x1="0" y1="-24" x2="0" y2="24"/>
        <line x1="-24" y1="0" x2="24" y2="0"/>
        <line x1="-20" y1="-12" x2="20" y2="-12"/>
        <line x1="-20" y1="12" x2="20" y2="12"/>
      </g>
      <text class="web" x="115" y="905" textLength="287" lengthAdjust="spacingAndGlyphs">www.quillclearing.com</text>

      <g class="icon handset" transform="translate(430 860)">
        <path d="M8 2 L16 14 L11 20 C14 28 20 34 28 38 L34 33 L46 41 L42 50 C22 50 0 28 0 8 Z"/>
        <path d="M30 14 A10 10 0 0 1 38 22"/>
        <path d="M30 4 A20 20 0 0 1 48 22"/>
      </g>
      <text class="phone" x="499" y="914" textLength="289" lengthAdjust="spacingAndGlyphs">412-555-0183</text>
    </svg>
  </main>
</body>
</html>
```